BRAVELUX Program Cover

Every year, we host an annual conference for educators who teach in afterschool in the Southwest. This year, we are renaming the conference to BRAVELUX 2014 (stands for Beyond-Bell-Hours Learning Summit). The theme of our conference is made up of three verbs: Innovate, Collaborate, & Thrive. We are looking for a program cover that is creative and yet visually appealing to an audience that ranges from Millennials to Baby Boomers. It needs to convey the three verbs and also brand the conference with the new name. We like the colors Blue and Green as our previous programs have been red, gold, yellow, and orange. Our audience teaches kids from K - 12, but likes to be treated as professionals (not the typical school clipart stuff). The conference is hosted at the Ft. Worth Calloway Lodge from July 23rd to July 24th, 2014. The program cover will set the tone for all conference materials (i.e. color scene, potential logo, etc...).

Target Market(s)

The target audience is participants of the conference. The age ranges from 25 to 60, but they are all either teachers, social workers, or educational administrators. All have a Bachelor's Degree or higher. While they are professionals, they also like to have fun.

Industry/Entity Type

Graphic Design

Requirements
Must have
• BRAVELUX must be prevalent and tagged with Beyond-Bell-Hours Learning Summit so that people know what it stands for.
Should not have
• The design should be clean with zero clipart.

```html
<!DOCTYPE html>
<html lang="en">
<head>
<meta charset="utf-8">
<title>BRAVELUX Program Cover</title>
<link rel="stylesheet" href="https://fonts.googleapis.com/css2?family=Montserrat:wght@300;400;500;600&display=swap">
<style>
  :root {
    --brand-blue: #0a8fc9;
    --brand-green: #87b23d;
    --ink: #3d4143;
    --tag-grey: #e3e5e6;
    --frame: #b4b7b9;
    --paper: #ffffff;
    --sun: #f6e08a;
    --sky: #cfe6f1;
    --leaf: #c9dd8c;
  }
  html, body {
    margin: 0;
    padding: 0;
    width: 928px;
    height: 1200px;
    overflow: hidden;
    background: var(--paper);
  }
  .cover {
    position: relative;
    width: 928px;
    height: 1200px;
    box-sizing: border-box;
    border: 3px solid var(--frame);
    background: var(--paper);
    font-family: "Montserrat", Arial, sans-serif;
    overflow: hidden;
  }
  .cover__title {
    position: absolute;
    left: 56px;
    top: 14px;
    margin: 0;
    font-weight: 600;
    font-size: 134px;
    line-height: 1;
    letter-spacing: -2px;
    color: var(--brand-blue);
  }
  .cover__tagline-box {
    position: absolute;
    left: 70px;
    top: 204px;
    width: 392px;
    height: 90px;
    background: var(--tag-grey);
    display: flex;
    flex-direction: column;
    justify-content: center;
    align-items: center;
    color: var(--ink);
    font-weight: 500;
    font-size: 24px;
    line-height: 1.2;
    letter-spacing: 1px;
    text-align: center;
  }
  .cover__year {
    position: absolute;
    left: 470px;
    top: 166px;
    margin: 0;
    font-weight: 600;
    font-size: 160px;
    line-height: 1;
    letter-spacing: -8px;
    color: var(--brand-green);
  }
  .cover__theme {
    position: absolute;
    left: 68px;
    top: 318px;
    margin: 0;
    font-weight: 300;
    font-size: 31px;
    letter-spacing: 3.6px;
    color: var(--ink);
    white-space: nowrap;
  }
  .cover__theme-divider {
    padding: 0 10px;
  }
  .cover__artwork {
    position: absolute;
    left: 0;
    top: 370px;
    width: 922px;
    height: 824px;
    background:
      radial-gradient(circle at 56% 72%, var(--sun) 0, rgba(246,224,138,0.5) 14%, rgba(246,224,138,0) 36%),
      radial-gradient(ellipse at 85% 10%, var(--leaf) 0, rgba(201,221,140,0) 28%),
      radial-gradient(ellipse at 22% 48%, var(--sky) 0, rgba(207,230,241,0) 50%),
      linear-gradient(180deg, #ffffff 0%, #f2f8ec 60%, #e4f1f6 100%);
  }
  .cover__details {
    position: absolute;
    left: 68px;
    top: 1050px;
    margin: 0;
    font-weight: 400;
    font-size: 19px;
    line-height: 1.3;
    color: var(--ink);
  }
</style>
</head>
<body>
  <main class="cover">
    <h1 class="cover__title">BRAVELUX</h1>
    <div class="cover__tagline-box">
      <span>BEYOND-BELL-HOURS</span>
      <span>LEARNING SUMMIT</span>
    </div>
    <p class="cover__year">2014</p>
    <p class="cover__theme">INNOVATE<span class="cover__theme-divider">I</span>COLLABORATE<span class="cover__theme-divider">I</span>THRIVE</p>
    <div class="cover__artwork" role="img" aria-label="Soft illustration of sun rays rising behind pale blue clouds, green rolling hills and a slender tree with a green canopy"></div>
    <p class="cover__details">July 23 - 24<br>Ft. Worth Calloway Lodge</p>
  </main>
</body>
</html>
```